Poster Title Design

Create a text design concept for a documentary film called:
"The Orchard Beekeepers"
Background should be black, design elements and text should be red and/or white.
Design should be bold and readable from a distance.
Please provide at least 3 alternative concepts per submission.
(No need to include images or illustrations in the design. We only need a text treatment with optional simple graphic lines curves or blocks. There are no existing show logos.)
Please submit concepts centered in frame, 1200 wide x 1000 high jpg.
Thanks!
Good Luck!
- please use solid read and white colors for text and design elements.
- please do not use any fonts in the courier family.
please do not use any script or shadow fonts.
please do not use any other colors than red, white and black.
please avoid using gradients.
no need to include images or illustrations, just need the title text treatment.

```html
<!DOCTYPE html>
<html lang="en">
<head>
<meta charset="utf-8">
<title>The Orchard Beekeepers — Title Treatment</title>
<link rel="stylesheet" href="https://fonts.googleapis.com/css2?family=Jost:wght@600&display=swap">
<style>
  :root {
    --paper: #ffffff;
    --poster-red: #ee2226;
    --poster-black: #000000;
    --title-white: #ffffff;
  }
  * { margin: 0; padding: 0; box-sizing: border-box; }
  html, body {
    width: 1200px;
    height: 1000px;
    overflow: hidden;
    background: var(--paper);
  }
  .canvas {
    position: relative;
    width: 1200px;
    height: 1000px;
    background: var(--paper);
  }
  .poster {
    position: absolute;
    left: 283px;
    top: 23px;
    width: 566px;
    height: 957px;
    background: var(--poster-black);
    border: 34px solid var(--poster-red);
  }
  .title {
    font-weight: 600;
  }
  .title-line {
    position: absolute;
    display: block;
    left: 283px;
    width: 566px;
    text-align: center;
    white-space: nowrap;
    font-family: "Jost", "Futura", sans-serif;
    font-weight: 600;
    line-height: 1;
    color: var(--title-white);
  }
  .title-the {
    top: 356px;
    font-size: 44px;
    letter-spacing: 4px;
    padding-left: 4px;
  }
  .title-orchard {
    top: 410px;
    font-size: 66px;
    letter-spacing: 2px;
    padding-left: 2px;
  }
  .title-beekeepers {
    top: 596px;
    font-size: 46px;
    letter-spacing: 9px;
    padding-left: 9px;
  }
</style>
</head>
<body>
  <main class="canvas">
    <div class="poster"></div>
    <h1 class="title">
      <span class="title-line title-the">THE</span>
      <span class="title-line title-orchard">ORCHARD</span>
      <span class="title-line title-beekeepers">BEEKEEPERS</span>
    </h1>
  </main>
</body>
</html>
```